Infographic Table of AI Pricing Options for LinkedIn post

Turn this table (in the powerpoint slide attached) into an attractively formatted infographic table for Strelquin (www.strelquin.com).
This will be an infographic displayed on a linkedin post from a consultant from Strelquin.
Try to keep it on brand with Strelquin look and feel.

Target Market(s)

Tech and SaaS CEOs and Founders; Private Equity and Venture Capital employees

Industry/Entity Type

Management Consulting

Colors
0054AA
0677BA
7BADD7
CADEEF
E8F1F8

```html
<!DOCTYPE html>
<html lang="en">
<head>
<meta charset="UTF-8">
<title>Challenges of GenAI Monetization — Strelquin</title>
<link href="https://fonts.googleapis.com/css2?family=Montserrat:wght@500;700;800&display=swap" rel="stylesheet">
<style>
  :root{
    --navy:#14283f;
    --ink:#1a2b45;
    --teal:#5fc4c4;
    --tab-a:#5cc3c4;
    --tab-b:#4aa2d8;
    --pros:#7badd7;
    --cons:#cadeef;
    --pill-a:#5aa8a2;
    --pill-b:#3b4150;
    --brand-blue:#0677ba;
    --accent:#0054aa;
    --white:#ffffff;
  }
  *{box-sizing:border-box;margin:0;padding:0}
  html,body{width:1200px;height:958px;overflow:hidden;background:var(--white)}
  body{font-family:'Montserrat',sans-serif;color:var(--ink);position:relative}
  .abs{position:absolute}
  .header{left:0;top:0;width:1181px;height:92px;background:var(--navy)}
  .brand{left:14px;top:38px;color:var(--white);font-weight:700;font-size:10px;letter-spacing:.3px}
  .title{left:111px;top:18px;color:var(--white);font-weight:800;font-size:45px;letter-spacing:2.4px;line-height:56px;white-space:nowrap}
  .pill{top:127px;height:35px;border-radius:18px;border:1px solid #2c4a52;
    background:linear-gradient(90deg,var(--pill-a),var(--pill-b));color:var(--white);
    font-weight:800;font-size:16px;letter-spacing:1.2px;display:flex;align-items:center;justify-content:center}
  .tab{top:186px;width:220px;height:114px}
  .tab svg{position:absolute;left:0;top:0}
  .tab-name{position:absolute;left:0;width:220px;text-align:center;color:var(--white);font-weight:800;font-size:16.5px;letter-spacing:1.2px;line-height:20px}
  .tab-letter{position:absolute;left:0;width:220px;text-align:center;top:66px;color:var(--white);font-weight:800;font-size:40px;line-height:44px}
  .icon{top:312px}
  .band{left:11px;width:1189px}
  .band-desc{top:387px;height:132px;background:var(--teal)}
  .band-pros{top:676px;height:132px;background:var(--pros)}
  .band-cons{top:827px;height:131px;background:var(--cons)}
  .row-label{font-weight:800;font-size:12.5px;letter-spacing:.6px;color:var(--ink)}
  .cell{font-weight:800;font-size:12.5px;line-height:15.3px;letter-spacing:.5px;text-transform:uppercase;color:var(--ink)}
  .cell ul{list-style:none}
  .cell li{padding-left:9px;position:relative}
  .cell li::before{content:"▪";position:absolute;left:0;font-size:8px}
  .brand-name{font-weight:700;font-size:21px;color:var(--ink);white-space:nowrap;display:flex;align-items:center;gap:9px}
  .brand-sq{width:40px;height:40px;border-radius:8px;background:var(--brand-blue)}
  .brand-dot{width:20px;height:20px;border-radius:50%;background:var(--brand-blue)}
  .note{font-weight:700;font-size:12.5px;color:var(--ink)}
  .sub{font-weight:500;font-size:13px;color:var(--ink)}
</style>
</head>
<body>
  <div class="abs header"></div>
  <div class="abs brand">Strelquin</div>
  <h1 class="abs title">CHALLENGES OF GENAI MONETIZATION</h1>

  <div class="abs pill" style="left:214px;width:534px">FREQUENTLY SEEN TODAY</div>
  <div class="abs pill" style="left:858px;width:216px">FUTURE OPTION?</div>

  <svg width="0" height="0" style="position:absolute">
    <defs>
      <linearGradient id="tabGrad" x1="0" y1="0" x2="1" y2="1">
        <stop offset="0" stop-color="#5cc3c4"/>
        <stop offset="1" stop-color="#4aa2d8"/>
      </linearGradient>
    </defs>
  </svg>

  <div class="abs tab" style="left:146px">
    <svg width="220" height="114"><path d="M0.5,12 Q0.5,0.5 12,0.5 H208 Q219.5,0.5 219.5,12 V78 H167 A65 65 0 0 1 53 78 H0.5 Z" fill="url(#tabGrad)" stroke="#1f3a4a" stroke-width="1"/></svg>
    <div class="tab-name" style="top:29px">USER LICENSES</div>
    <div class="tab-letter">A</div>
  </div>
  <div class="abs tab" style="left:382px">
    <svg width="220" height="114"><path d="M0.5,12 Q0.5,0.5 12,0.5 H208 Q219.5,0.5 219.5,12 V78 H167 A65 65 0 0 1 53 78 H0.5 Z" fill="url(#tabGrad)" stroke="#1f3a4a" stroke-width="1"/></svg>
    <div class="tab-name" style="top:29px">USER-BASED TOKEN</div>
    <div class="tab-letter">B</div>
  </div>
  <div class="abs tab" style="left:622px">
    <svg width="220" height="114"><path d="M0.5,12 Q0.5,0.5 12,0.5 H208 Q219.5,0.5 219.5,12 V78 H167 A65 65 0 0 1 53 78 H0.5 Z" fill="url(#tabGrad)" stroke="#1f3a4a" stroke-width="1"/></svg>
    <div class="tab-name" style="top:29px">OUTCOME-BASED</div>
    <div class="tab-letter">C</div>
  </div>
  <div class="abs tab" style="left:861px">
    <svg width="220" height="114"><path d="M0.5,12 Q0.5,0.5 12,0.5 H208 Q219.5,0.5 219.5,12 V78 H167 A65 65 0 0 1 53 78 H0.5 Z" fill="url(#tabGrad)" stroke="#1f3a4a" stroke-width="1"/></svg>
    <div class="tab-name" style="top:18px">USAGE-TIERED<br>LICENSES</div>
    <div class="tab-letter">D</div>
  </div>

  <!-- icons -->
  <svg class="abs icon" style="left:232px" width="48" height="58" viewBox="0 0 48 58" aria-label="Licence document">
    <path d="M10 2 H42 V52 H3 V9 Z" fill="none" stroke="var(--navy)" stroke-width="2.5"/>
    <path d="M3 9 H10 V2" fill="none" stroke="var(--navy)" stroke-width="2"/>
    <g stroke="var(--navy)" stroke-width="2"><line x1="12" y1="14" x2="34" y2="14"/><line x1="9" y1="21" x2="36" y2="21"/><line x1="9" y1="28" x2="36" y2="28"/><line x1="9" y1="35" x2="24" y2="35"/></g>
    <circle cx="31" cy="42" r="6" fill="var(--navy)"/>
    <path d="M27 47 L26 55 L31 52 L36 55 L35 47" fill="none" stroke="var(--navy)" stroke-width="1.8"/>
  </svg>
  <svg class="abs icon" style="left:456px;top:320px" width="108" height="45" viewBox="0 0 108 45" aria-label="Token key">
    <rect x="2" y="3" width="80" height="39" rx="12" fill="none" stroke="var(--navy)" stroke-width="3"/>
    <rect x="7" y="8" width="70" height="29" rx="8" fill="none" stroke="var(--navy)" stroke-width="2.5"/>
    <text x="42" y="30" text-anchor="middle" font-family="Montserrat,sans-serif" font-weight="800" font-size="20" fill="var(--navy)">****</text>
    <path d="M82 16 H88 V29 H82" fill="none" stroke="var(--navy)" stroke-width="2.5"/>
    <circle cx="96" cy="22.5" r="8" fill="none" stroke="var(--navy)" stroke-width="2.5"/>
  </svg>
  <svg class="abs icon" style="left:698px" width="76" height="66" viewBox="0 0 76 66" aria-label="Target with rising arrow">
    <circle cx="42" cy="18" r="16" fill="none" stroke="var(--navy)" stroke-width="1.8"/>
    <circle cx="42" cy="18" r="10.5" fill="none" stroke="var(--navy)" stroke-width="1.8"/>
    <circle cx="42" cy="18" r="5" fill="none" stroke="var(--navy)" stroke-width="1.8"/>
    <path d="M2 63 L22 43 L30 50 L62 18" fill="none" stroke="var(--navy)" stroke-width="1.8"/>
    <path d="M6 63 L22 47 L30 54 L64 22" fill="none" stroke="var(--navy)" stroke-width="1.8"/>
    <path d="M56 14 L70 12 L68 26 Z" fill="none" stroke="var(--navy)" stroke-width="1.8"/>
    <line x1="48" y1="54" x2="70" y2="32" stroke="var(--navy)" stroke-width="1.5"/>
  </svg>
  <svg class="abs icon" style="left:944px" width="58" height="60" viewBox="0 0 58 60" aria-label="Stacked layers">
    <path d="M29 2 L56 16 L29 30 L2 16 Z" fill="var(--navy)"/>
    <path d="M6 25 L2 27 L29 41 L56 27 L52 25" fill="none" stroke="var(--navy)" stroke-width="3.5" stroke-linejoin="round"/>
    <path d="M6 36 L2 38 L29 52 L56 38 L52 36" fill="none" stroke="var(--navy)" stroke-width="3.5" stroke-linejoin="round"/>
  </svg>

  <!-- description -->
  <div class="abs band band-desc"></div>
  <div class="abs row-label" style="left:33px;top:437px">DESCRIPTION</div>
  <div class="abs cell" style="left:176px;top:415px">Charge a flat<br>price for a user<br>to have access to<br>the functionality</div>
  <div class="abs cell" style="left:450px;top:415px">Purchase blocks of<br>tokens that can be<br>spend on<br>usage/work of the<br>AI functionality</div>
  <div class="abs cell" style="left:687px;top:415px">Pay for the<br>outcomes of<br>the GenAI<br>functionality</div>
  <div class="abs cell" style="left:939px;top:415px">Offer different<br>user licenses<br>with different<br>usage capacities</div>

  <!-- examples -->
  <div class="abs row-label" style="left:44px;top:592px">EXAMPLES</div>
  <div class="abs brand-name" style="left:176px;top:555px"><span class="brand-sq"></span>TalkForge</div>
  <div class="abs brand-name" style="left:180px;top:612px"><span class="brand-dot"></span>Wingmate</div>
  <div class="abs brand-name" style="left:453px;top:561px"><span class="brand-dot"></span>Luminar Labs</div>
  <div class="abs" style="left:504px;top:600px;width:28px;height:28px;border-radius:50%;background:var(--brand-blue)"></div>
  <div class="abs sub" style="left:462px;top:644px">Skyline Vision API</div>
  <div class="abs brand-name" style="left:694px;top:561px"><span class="brand-dot"></span>Deskwell</div>
  <div class="abs brand-name" style="left:691px;top:611px"><span class="brand-dot"></span>Disputera</div>
  <div class="abs brand-name" style="left:943px;top:555px"><span class="brand-sq"></span>TalkForge</div>
  <div class="abs note" style="left:945px;top:612px">kinda...</div>

  <!-- pros -->
  <div class="abs band band-pros"></div>
  <svg class="abs" style="left:64px;top:702px" width="55" height="52" viewBox="0 0 55 52" aria-label="Tick">
    <circle cx="25" cy="28" r="21" fill="none" stroke="var(--accent)" stroke-width="4"/>
    <path d="M13 27 L23 39 L50 3" fill="none" stroke="var(--accent)" stroke-width="6" stroke-linecap="round" stroke-linejoin="round"/>
  </svg>
  <div class="abs row-label" style="left:71px;top:762px">PROS</div>
  <div class="abs cell" style="left:176px;top:726px">Simple and easily<br>understood</div>
  <div class="abs cell" style="left:458px;top:708px"><ul><li>Covers costs at all<br>scales of usage</li><li>Tokens help with<br>predictability issues</li></ul></div>
  <div class="abs cell" style="left:707px;top:717px">Potentially<br>highly<br>value-aligned</div>
  <div class="abs cell" style="left:947px;top:685px"><ul><li>Value aligned</li><li>Simple &amp;<br>predictable</li><li>Natural<br>upsell path</li><li>Low barrier<br>to adoption</li></ul></div>

  <!-- cons -->
  <div class="abs band band-cons"></div>
  <svg class="abs" style="left:64px;top:862px" width="48" height="44" viewBox="0 0 48 44" aria-label="Cross">
    <circle cx="22" cy="21" r="19" fill="none" stroke="var(--accent)" stroke-width="4"/>
    <path d="M14 11 L32 31 M32 11 L14 31" stroke="var(--accent)" stroke-width="5" stroke-linecap="round"/>
  </svg>
  <div class="abs row-label" style="left:66px;top:911px">CONS</div>
  <div class="abs cell" style="left:185px;top:832px"><ul><li>High price limits adoption</li><li>Not tightly value aligned</li><li>Risky if fair usage<br>restriction is not placed<br>on</li><li>Upsell dependent on<br>wider adoption</li></ul></div>
  <div class="abs cell" style="left:458px;top:849px"><ul><li>Not tightly value<br>aligned (value may<br>not increase<br>linearly with usage)</li><li>Not ARR</li></ul></div>
  <div class="abs cell" style="left:695px;top:849px"><ul><li>Delayed revenue<br>realization</li><li>Not ARR</li><li>Tough to find the<br>right metric</li></ul></div>
  <div class="abs cell" style="left:947px;top:872px"><ul><li>Limit on the<br>number of<br>tiers</li></ul></div>
</body>
</html>
```